Human Resources consulting firm website

I recently started a consulting firm after 30 years in Human Resources (Executive Development) work with Meridian 25 companies. I am looking for a website design that will convey both the services I provide (all in the HR / executive development arena) as well as sense of trust in me and my abilities (many years of experience, breadth of knowledge).

In the attachment section, there is a document with links to a number of websites fr firms that do similar work to me - the doc shares what I like about them and what I do not. I've also include my bio to give you a sens of who I am /what I do. The head shot will be replaced soon as I'm having new photos take, but the verbiage is what's important.

I need your help with the look and feel as well as different ideas on how to share the info. I am looking for your creativity and experience. I have not done a website for anything in the past.

Looking forward to working together on a great project and product!!

Target Market(s)

Any company looking for senior leader caoching, assessments of those leaders or help with a CEO transition. My wheelhouse is Meridian top 100 companies, but am able to work with small firms as well. Also any Board of Directors and upstarts in California.

Industry/Entity Type

Consulting

Coding

Coded - Design and coding required

Number of Pages Required

5+ page

Font styles to use
Sans Serif
Other font styles liked:
• Do not have a specific one but am very open to options

Colors

Designer to choose colors to be used in the design.

Requirements
Must have
• My project must have be professional (see the type of companies I am targeting) with an air of simplicity.
• A professional yet approachable look and feel that delivers:
• (1) I want there to be a landing page (with limited info - a more of a "teaser")
• (2) a tab for about us (with a few sentences about the company, my photo and option to link to my bio)
• (3) a tab for the services offered (one page with tiles that have a little bit about the services and the option to link to more info)
• (4) a tab to contact me (form to fill out with some personal info and the request that will get sent to my email).
• (5) diversity in the imagery
• (6) I plan for it to be mostly static. I will not be adding/changing regularly (although imagine the first couple months will want to tweak it as I get feedback). I do not plan to add blogs, etc.
Nice to have
• (1) Good graphics. I'm ok with black and white if it's classic or color photos. I don't want stalk photos anyone can get on the web. A sophisticated yet approachable look is what I'm going for.
• (2) Ability to get to know me (the principal) just a bit. That can be through the verbiage, colors, photos, etc.
• (3) Ability to contact me from the front home/landing page or contact page.
• (4) When someone looks me up on line, I want them to see a sentence or two about the company and have links that will take them straight to the page on the website they are looking for (contact, about us, etc.)
Should not have
• I do not want this to be:
• (1) overly feminine (not pink, purple, etc.),
• (2) flashy (I'm fine with a small video or moving photo but doubt I want anything beyond that) or
• (3) too close to the "out there" category (this is a professional business with corporate clients).
• (4) sterile (I'm selling myself .. that's what people buy when they hire a consultant).
• (5) basic - I do not want this to look like I hired my nephew straight out of college to build this. I'm looking for a strong, professional look.

```html
<!DOCTYPE html>
<html lang="en">
<head>
<meta charset="utf-8">
<title>Harborview Talent Solutions</title>
<link href="https://fonts.googleapis.com/css2?family=Montserrat:wght@400;500;600;700&family=Open+Sans:wght@400;600&display=swap" rel="stylesheet">
<style>
:root{
  --blue:#5b8fd3;
  --blue-soft:#8fb3e0;
  --navy:#2f3a4a;
  --ink:#3a3f47;
  --muted:#8a9099;
  --line:#d5d9df;
  --paper:#ffffff;
  --fog:#eef1f5;
}
*{box-sizing:border-box;margin:0;padding:0}
html,body{width:1200px;height:2716px;overflow:hidden;background:var(--paper)}
body{font-family:"Open Sans",Arial,sans-serif;color:var(--ink);position:relative}
h1,h2,h3,.brand,.nav,.btn{font-family:"Montserrat",Arial,sans-serif}
.abs{position:absolute}

/* header */
.site-header{position:absolute;top:0;left:0;width:1200px;height:100px;z-index:5;display:flex;align-items:center;padding:0 72px}
.brand{display:flex;align-items:center;gap:14px;color:var(--paper);font-weight:600;font-size:15px;letter-spacing:1.5px;line-height:1.25;text-transform:uppercase}
.brand-mark{width:40px;height:40px;background:var(--blue)}
.nav{margin-left:auto;display:flex;align-items:center;gap:46px;font-size:17px;font-weight:600;color:var(--paper)}
.nav .active{color:var(--blue-soft);border-bottom:2px solid var(--blue-soft);padding-bottom:4px}
.btn{display:inline-block;font-size:16px;font-weight:600;border-radius:30px;padding:12px 34px}
.btn-solid{background:var(--blue);color:var(--paper)}
.btn-ghost-light{border:2px solid var(--paper);color:var(--paper)}
.btn-ghost{border:2px solid var(--line);color:var(--blue)}
.social{display:flex;gap:14px;margin-left:-16px}
.social span{width:40px;height:40px;border-radius:50%;background:#9aa0a8;display:block}

/* hero */
.hero-photo{left:0;top:0;width:1200px;height:640px;background:linear-gradient(120deg,#6b7178 0%,#9a9ea3 45%,#c8cbce 70%,#7b8087 100%)}
.hero-shade{left:0;top:0;width:1200px;height:640px;background:linear-gradient(90deg,rgba(30,35,42,.55),rgba(30,35,42,0) 55%)}
.hero-text{left:90px;top:236px;color:var(--paper)}
.hero-text h1{font-size:50px;font-weight:600}
.hero-text p{font-size:26px;font-weight:500;font-family:"Montserrat",Arial,sans-serif;margin:14px 0 36px}

/* about */
.about-frame{left:236px;top:728px;width:296px;height:340px;border:2px solid var(--line)}
.about-photo{left:206px;top:700px;width:296px;height:340px;background:linear-gradient(160deg,#d8dadd,#8e9298 60%,#5a5e64)}
.about-rule{left:610px;top:700px;width:2px;height:330px;background:var(--line)}
.about-copy{left:640px;top:716px;width:360px}
.about-copy h2{font-size:29px;font-weight:500;line-height:1.3;color:var(--navy)}
.about-copy h2 em{font-style:normal;color:var(--blue)}
.about-copy p{font-size:13px;line-height:1.7;color:var(--muted);margin-top:22px}
.about-copy .btn{margin-top:30px;padding:10px 30px;font-size:14px}

/* services */
.services{left:0;top:1170px;width:1200px;height:440px;background:linear-gradient(100deg,#8db0dd,#b6cbe6 50%,#98b6de)}
.section-title{width:1200px;text-align:center;font-size:30px;font-weight:500;color:var(--navy)}
.section-title em{font-style:normal;color:var(--blue)}
.services .section-title{position:absolute;top:80px;color:var(--paper)}
.services .section-title em{color:#2f5f9e}
.tile{position:absolute;top:150px;width:312px;height:212px;background:linear-gradient(150deg,#7c8188,#4f545b);color:var(--paper);font-family:"Montserrat",Arial,sans-serif}
.tile h3{position:absolute;left:0;right:0;bottom:22px;text-align:center;font-size:19px;font-weight:600}
.tile.featured h3{top:28px;bottom:auto}
.tile.featured p{position:absolute;top:66px;left:50px;right:50px;text-align:center;font-size:12px;line-height:1.5;font-family:"Open Sans",Arial,sans-serif}
.tile.featured .more{position:absolute;left:0;right:0;top:130px;text-align:center;font-size:13px;font-weight:600}
.tile.featured .more span{border-bottom:1px solid var(--paper)}

/* reviews */
.reviews .section-title{position:absolute;top:1668px;left:0}
.avatar{left:570px;top:1742px;width:60px;height:60px;border-radius:50%;background:linear-gradient(#c9a98f,#8d7766)}
.quote{left:290px;top:1840px;width:620px;text-align:center;font-size:15px;font-style:italic;line-height:1.7;color:var(--muted)}
.reviewer{left:0;top:1952px;width:1200px;text-align:center;font-size:15px;font-weight:600;color:var(--navy)}
.reviewer small{display:block;font-size:11px;font-weight:400;color:var(--muted);margin-top:4px}
.view-all{left:538px;top:2018px;padding:10px 34px;font-size:14px}

/* cta */
.cta{left:0;top:2120px;width:1200px;height:160px;background:linear-gradient(100deg,#8fb1dd,#a9c1e2 60%,#8aa7d2)}
.cta h2{position:absolute;left:90px;top:60px;font-size:30px;font-weight:500;color:var(--paper)}
.cta h2 strong{font-weight:600;color:#2f5f9e}
.cta .btn{position:absolute;right:100px;top:52px}

/* footer */
.contact-col{left:90px;top:2340px;width:360px}
.label{font-family:"Montserrat",Arial,sans-serif;font-size:17px;font-weight:600;color:var(--navy)}
.label em{font-style:normal;color:var(--blue)}
.phone{font-family:"Montserrat",Arial,sans-serif;font-size:32px;color:var(--blue);margin-top:26px}
.contact-col .mail{font-size:12px;color:var(--muted);margin-top:6px;display:flex;align-items:center;gap:6px}
.contact-col .addr{font-size:12px;line-height:1.6;color:var(--muted);margin-top:18px}
.contact-col .addr b{color:var(--blue);font-weight:600;font-size:14px}
.form{left:470px;top:2340px;width:640px}
.form .row{display:flex;gap:12px;margin-top:26px}
.field{flex:1;height:36px;border:1px solid var(--line);border-radius:18px;font-size:12px;color:var(--muted);padding:10px 18px}
.field.area{height:96px;border-radius:12px;margin-top:12px}
.submit{margin-top:14px;padding:9px 32px;font-size:13px}
.copyright{left:90px;top:2680px;font-size:11px;color:var(--muted)}
.foot-rule{left:90px;top:2664px;width:1020px;height:1px;background:var(--line)}
</style>
</head>
<body>

<header class="site-header">
  <div class="brand"><span class="brand-mark"></span><span>Harborview<br>Talent<br>Solutions</span></div>
  <nav class="nav">
    <span class="active">Home</span><span>About Us</span><span>Services</span><span>Reviews</span>
    <span class="btn btn-solid">Contact Me</span>
    <span class="social"><span></span><span></span></span>
  </nav>
</header>

<div class="abs hero-photo" role="img" aria-label="Two businesswomen in discussion at a meeting table with a laptop"></div>
<div class="abs hero-shade"></div>
<svg class="abs" style="left:0;top:380px" width="1200" height="300" viewBox="0 0 1200 300">
  <path d="M0 190 C300 90 700 120 1200 40 L1200 300 L0 300Z" fill="var(--fog)" opacity=".7"/>
  <path d="M0 230 C320 130 760 160 1200 70 L1200 300 L0 300Z" fill="var(--paper)"/>
  <path d="M700 175 C900 140 1050 110 1200 60 L1200 80 C1050 120 900 150 700 182Z" fill="var(--blue-soft)"/>
</svg>
<div class="abs hero-text">
  <h1>Speaking &amp; Consulting</h1>
  <p>Building leaders &amp; teams, Shaping culture, Storytelling</p>
  <span class="btn btn-ghost-light">Contact Me</span>
</div>

<section class="about">
  <div class="abs about-frame"></div>
  <div class="abs about-photo" role="img" aria-label="Portrait of the principal consultant in a dark suit, arms folded"></div>
  <div class="abs about-rule"></div>
  <div class="abs about-copy">
    <h2>We Bring <em>30+ Years</em><br><em>of Talent Development</em><br>Expertise.</h2>
    <p>There are many variations of passages of Lorem Ipsum available, but the majority have suffered alteration in some form, by injected humour, or randomised words which don't look even slightly believable.</p>
    <p>If you are going to use a passage of Lorem Ipsum, you need to be sure there isn't anything embarrassing hidden in the middle of text of the Lorem Ipsum.</p>
    <span class="btn btn-ghost">About Me</span>
  </div>
</section>

<section class="abs services">
  <h2 class="section-title">Our <em>Services</em></h2>
  <div class="tile" style="left:88px" role="img" aria-label="Team gathered around a table in a workshop"><h3>Culture Growth</h3></div>
  <div class="tile featured" style="left:444px" role="img" aria-label="Leader presenting to a small group">
    <h3>Leadership Development</h3>
    <p>Coaching senior leaders to grow with clarity, confidence and a steady sense of purpose.</p>
    <div class="more"><span>Read More</span></div>
  </div>
  <div class="tile" style="left:800px" role="img" aria-label="Speaker addressing an audience in a conference room"><h3>Speaking &amp; Consulting</h3></div>
</section>

<section class="reviews">
  <h2 class="section-title">What Our <em>Clients Are Saying</em></h2>
  <div class="abs avatar" role="img" aria-label="Client portrait"></div>
  <p class="abs quote">“ There are many variations of passages of Lorem Ipsum available, but the majority have suffered alteration in some form, by injected humour, or randomised words which don't look even slightly believable. If you are going to use a passage of Lorem Ipsum ... ”</p>
  <div class="abs reviewer">Standard Chunk<small>Lorem Ipsum</small></div>
  <span class="abs btn btn-ghost view-all">View All</span>
</section>

<svg class="abs" style="left:0;top:2060px" width="1200" height="70" viewBox="0 0 1200 70">
  <path d="M0 70 L0 60 C400 60 800 40 1200 0 L1200 70Z" fill="#b9c8dc"/>
</svg>
<section class="abs cta">
  <h2>Let's Start a Conversation <strong>About Your Talent Needs.</strong></h2>
  <span class="btn btn-ghost-light">Contact Me</span>
</section>

<footer>
  <div class="abs contact-col">
    <div class="label">Contact <em>Us</em></div>
    <div class="phone">Call: (123) 456-7890</div>
    <div class="mail"><svg width="12" height="9" viewBox="0 0 12 9"><rect x=".5" y=".5" width="11" height="8" fill="none" stroke="#8a9099"/><path d="M.5 .5 6 5 11.5 .5" fill="none" stroke="#8a9099"/></svg>info@harborviewtalent.com</div>
    <div class="addr"><b>Address:</b><br>2200 Harbor Point Drive, Suite 310<br>Oakland, CA 94612</div>
  </div>
  <div class="abs form">
    <div class="label">Request a <em>Consulting</em></div>
    <div class="row"><div class="field">Name</div><div class="field">Email</div><div class="field">Phone</div></div>
    <div class="field area">Your Message</div>
    <span class="btn btn-solid submit">Submit</span>
  </div>
  <div class="abs foot-rule"></div>
  <div class="abs copyright">© 2024 Harborview Talent Solutions. All Rights Reserved.</div>
</footer>

</body>
</html>
```